Business Card Design

Attached is my current Business card I do not like it but I must save the logo portion of it. Don't like the color or the lettering am looking for more architectural look in grays or taupe with the green more of a charturese color and the blue a charcoal color on a textured paper that looks more like something high-end that would appeal to an architect or a designer. We make concrete decorative items such as concrete fireplaces, sinks, tops and more.

Target Market(s)

Architects designers of Commercial and Residential - artistic features

Industry/Entity Type

Architect

Contact Information for Business Card

Marla T. Quinby President and Marketing Director
602-471-8836
email marla@quillstoneworks.example
Showroom "Valtique Design Center" 4128 W Larkmoor Scottsdale AZ
Fax: 602-713-4429

Font styles to use
Sans Serif

Requirements
Must have
• Architectural
Natural and earthy colors with a touch of color in the existing attached

```html
<!DOCTYPE html>
<html lang="en">
<head>
<meta charset="utf-8">
<title>Quillstone Works – Business Card</title>
<link href="https://fonts.googleapis.com/css2?family=Exo+2:wght@300;400&display=swap" rel="stylesheet">
<style>
  :root {
    --canvas: #e4e2df;
    --card-gray: #747577;
    --card-light: #eeeeee;
    --chartreuse: #8fb021;
    --charcoal-blue: #2f4358;
    --text-light: #f2f2f2;
    --text-muted: #6a6c6f;
    --contact-text: #e6e6e6;
  }
  * { margin: 0; padding: 0; box-sizing: border-box; }
  html, body { width: 1200px; height: 1000px; overflow: hidden; }
  body {
    background: var(--canvas);
    font-family: "Exo 2", "Helvetica Neue", Arial, sans-serif;
    position: relative;
  }
  .card {
    position: absolute;
    left: 250px;
    width: 700px;
    height: 400px;
    overflow: hidden;
    box-shadow: 0 6px 18px rgba(0,0,0,0.18);
  }
  .card--back { top: 60px; background: var(--card-gray); }
  .card--front { top: 540px; background: var(--card-light); }

  /* Back side */
  .brand-block {
    position: absolute;
    left: 0; right: 0; top: 150px;
    text-align: center;
    color: var(--text-light);
  }
  .brand-block .brand-name {
    font-weight: 300;
    font-size: 44px;
    letter-spacing: 2px;
    text-transform: uppercase;
    display: inline-flex;
    align-items: center;
    gap: 16px;
  }
  .brand-square {
    width: 22px; height: 22px;
    background: var(--chartreuse);
    display: inline-block;
  }
  .brand-block .brand-tagline {
    font-weight: 300;
    font-size: 22px;
    margin-top: 6px;
    letter-spacing: 1px;
  }

  /* Front side */
  .front-shape { position: absolute; inset: 0; }
  .front-brand {
    position: absolute;
    right: 34px; top: 26px;
    text-align: right;
    color: var(--charcoal-blue);
  }
  .front-brand .brand-name {
    font-size: 15px;
    font-weight: 400;
    letter-spacing: 1px;
    text-transform: uppercase;
  }
  .front-brand .brand-tagline { font-size: 10px; font-weight: 300; }

  .person {
    position: absolute;
    left: 46px; top: 188px;
  }
  .person-name {
    color: var(--charcoal-blue);
    font-size: 40px;
    font-weight: 400;
  }
  .person-title {
    color: var(--text-muted);
    font-size: 15px;
    font-weight: 300;
    margin-top: 2px;
  }

  .showroom {
    position: absolute;
    left: 318px; top: 322px;
    font-size: 13px;
    font-weight: 300;
    color: var(--contact-text);
    line-height: 1.35;
  }
  .showroom-title {
    color: var(--chartreuse);
    display: flex; align-items: center; gap: 7px;
  }
  .showroom-address { padding-left: 19px; }

  .contact-list {
    position: absolute;
    right: 30px; top: 192px;
    list-style: none;
    font-size: 12px;
    font-weight: 300;
    color: var(--contact-text);
  }
  .contact-list li {
    display: flex; align-items: center; gap: 9px;
    margin-bottom: 9px;
    white-space: nowrap;
  }
  .contact-list svg, .showroom svg { flex: none; }
</style>
</head>
<body>

<section class="card card--back" aria-label="Business card back">
  <div class="brand-block">
    <div class="brand-name"><span class="brand-square"></span>Quillstone Works</div>
    <div class="brand-tagline">Design Studio</div>
  </div>
</section>

<section class="card card--front" aria-label="Business card front">
  <svg class="front-shape" width="700" height="400" viewBox="0 0 700 400" aria-hidden="true">
    <path d="M700,88 C480,118 285,220 226,400 L700,400 Z" fill="var(--chartreuse)"/>
    <path d="M700,95 C486,126 293,226 236,400 L700,400 Z" fill="var(--card-light)"/>
    <path d="M700,100 C490,132 300,230 243,400 L700,400 Z" fill="var(--charcoal-blue)"/>
    <path d="M700,108 C496,140 309,236 253,400 L700,400 Z" fill="var(--card-gray)"/>
  </svg>

  <div class="front-brand">
    <div class="brand-name">Quillstone Works</div>
    <div class="brand-tagline">Design Studio</div>
  </div>

  <div class="person">
    <div class="person-name">Marla T. Quinby</div>
    <div class="person-title">President &amp; Marketing Director</div>
  </div>

  <div class="showroom">
    <div class="showroom-title">
      <svg width="12" height="12" viewBox="0 0 12 12"><path d="M6 1 L11 6 H9.5 V11 H2.5 V6 H1 Z" fill="var(--charcoal-blue)"/></svg>
      Quillstone Works Showroom
    </div>
    <div class="showroom-address">"Valtique Design Center" 4128 W Larkmoor Scottsdale AZ</div>
  </div>

  <ul class="contact-list">
    <li>
      <svg width="12" height="12" viewBox="0 0 12 12"><path d="M2.5 1 L4.5 1 L5.3 3.6 L4 4.6 C4.7 6 5.9 7.3 7.4 8 L8.4 6.7 L11 7.5 L11 9.5 C11 10.3 10.3 11 9.5 11 C5 11 1 7 1 2.5 C1 1.7 1.7 1 2.5 1 Z" fill="var(--charcoal-blue)"/></svg>
      602-471-8836
    </li>
    <li>
      <svg width="12" height="12" viewBox="0 0 12 12"><rect x="1" y="4" width="10" height="7" rx="1" fill="var(--charcoal-blue)"/><rect x="3" y="1" width="6" height="4" fill="var(--charcoal-blue)"/><rect x="3.5" y="6.5" width="5" height="1.2" fill="var(--card-gray)"/></svg>
      602-713-4429
    </li>
    <li>
      <svg width="12" height="12" viewBox="0 0 12 12"><rect x="1" y="2.5" width="10" height="7" fill="var(--charcoal-blue)"/><path d="M1 2.5 L6 6.5 L11 2.5" fill="none" stroke="var(--card-gray)" stroke-width="1"/></svg>
      marla@quillstoneworks.example
    </li>
  </ul>
</section>

</body>
</html>
```